Bravel Acres Business Cards

design business cards for our new business should match my Corvane Quotations business cards

Contact Information for Business Card

2817 W 68th N St
Tulsa, OK 74592

Requirements
Must have
• should match logo colors

```html
<!DOCTYPE html>
<html lang="en">
<head>
<meta charset="utf-8">
<title>Bravel Acres Business Cards</title>
<link href="https://fonts.googleapis.com/css2?family=Poppins:ital,wght@0,300;0,400;0,600;1,600&display=swap" rel="stylesheet">
<style>
  :root {
    --stage: #1c1d1f;
    --card-dark: #1b3840;
    --card-dark-edge: #16303a;
    --leaf-green: #7dc142;
    --aqua: #17b0b4;
    --paper: #ffffff;
    --pattern-tone: #e3f0f1;
    --ink-dark: #173039;
  }
  * { box-sizing: border-box; margin: 0; padding: 0; }
  html, body { width: 1200px; height: 900px; overflow: hidden; }
  body {
    background: var(--stage);
    font-family: "Poppins", sans-serif;
    display: flex;
    flex-direction: column;
    align-items: center;
    justify-content: center;
    gap: 36px;
  }
  .card {
    position: relative;
    width: 700px;
    height: 400px;
    border-radius: 4px;
    overflow: hidden;
  }
  /* Front */
  .card--front {
    background: linear-gradient(135deg, var(--card-dark) 0%, var(--card-dark-edge) 100%);
    color: var(--paper);
  }
  .holder { position: absolute; left: 56px; top: 52px; }
  .holder__name {
    font-weight: 600;
    font-style: italic;
    font-size: 24px;
    letter-spacing: 2px;
    text-transform: uppercase;
  }
  .holder__role {
    font-weight: 600;
    font-style: italic;
    font-size: 17px;
    letter-spacing: 1px;
    color: var(--leaf-green);
    text-transform: uppercase;
    margin-top: 2px;
  }
  .brand {
    position: absolute;
    display: flex;
    align-items: center;
    gap: 14px;
  }
  .brand__dot {
    width: 22px; height: 22px; border-radius: 50%;
    background: var(--leaf-green);
    flex: none;
  }
  .brand__name {
    font-weight: 600;
    font-size: 38px;
    letter-spacing: 5px;
    text-transform: uppercase;
    line-height: 1;
  }
  .card--front .brand { right: 52px; top: 150px; }
  .card--front .brand__name { color: var(--paper); }
  .divider {
    position: absolute;
    left: 56px; right: 56px; top: 262px;
    height: 1px;
    background: var(--paper);
    opacity: 0.85;
  }
  .contacts {
    position: absolute;
    left: 56px; top: 284px;
    list-style: none;
    font-size: 17px;
    font-weight: 300;
    line-height: 1.7;
  }
  .contacts li, .address { display: flex; align-items: center; gap: 12px; }
  .icon { width: 16px; height: 16px; flex: none; }
  .address {
    position: absolute;
    right: 56px; top: 284px;
    align-items: flex-start;
    font-size: 17px;
    font-weight: 300;
    line-height: 1.5;
  }
  .address .icon { margin-top: 5px; }
  /* Back */
  .card--back { background: var(--paper); }
  .card--back .pattern {
    position: absolute; inset: 0;
    background: linear-gradient(135deg, var(--pattern-tone) 0%, #f4f9f9 50%, var(--pattern-tone) 100%);
  }
  .card--back .brand {
    left: 50%; top: 50%;
    transform: translate(-50%, -50%);
    background: var(--paper);
    padding: 22px 34px;
    border-radius: 4px;
  }
  .card--back .brand__name { color: var(--ink-dark); font-size: 46px; }
</style>
</head>
<body>
  <section class="card card--front">
    <div class="holder">
      <p class="holder__name">Darel Wyncote</p>
      <p class="holder__role">Managing Director</p>
    </div>
    <div class="brand">
      <span class="brand__dot"></span>
      <span class="brand__name">Bravel Acres</span>
    </div>
    <div class="divider"></div>
    <ul class="contacts">
      <li>
        <svg class="icon" viewBox="0 0 16 16"><path fill="var(--leaf-green)" d="M4 1l2.5 3-1.5 1.6c.8 1.9 2.3 3.5 4.3 4.4L11 8.5l3 2.4-1.3 2.6C7 13.5 2.5 9 2 3.3z"/></svg>
        <span>5550-2817-6840</span>
      </li>
      <li>
        <svg class="icon" viewBox="0 0 16 16"><rect x="1" y="3" width="14" height="10" rx="1" fill="var(--leaf-green)"/><path d="M1.5 3.5L8 9l6.5-5.5" fill="none" stroke="var(--card-dark)" stroke-width="1.3"/></svg>
        <span>info@bravelacres.com</span>
      </li>
    </ul>
    <div class="address">
      <svg class="icon" viewBox="0 0 16 16"><path fill="var(--aqua)" d="M8 1a5 5 0 0 0-5 5c0 3.8 5 9 5 9s5-5.2 5-9a5 5 0 0 0-5-5zm0 7a2 2 0 1 1 0-4 2 2 0 0 1 0 4z"/></svg>
      <span>2817 W 68th N St<br>Tulsa, OK 74592</span>
    </div>
  </section>

  <section class="card card--back">
    <div class="pattern" role="img" aria-label="Faint repeating brand pattern in pale aqua"></div>
    <div class="brand">
      <span class="brand__dot"></span>
      <span class="brand__name">Bravel Acres</span>
    </div>
  </section>
</body>
</html>
```